Hello - we need a label design for our Corvane Medical Hair Loss supplement. It is a natural hair loss supplement for black/african american women to regrow new hair and help restore hair loss & thinning hair due to vitamin deficiencies, traction alopecia, etc. It is a science based efficacious supplement with a centuries old medicinal herbal formula.
Attached is the logo & files of other generic competition and also Black hair products for your perusal. The label has to be a upscale and have an ethnic flair to it. The product is clinically effective, leveraged by Ancient Wisdom and Modern Science. The front of the label should include the following:
Corvane Medical (logo)
Root Revival
ELEVATED Women’s Hair Loss Formula
TRACTION ALOPECIA SUPPORT
- Prevents hair loss & restores thinning, fragile hair
- Promotes Natural Hair Growth
- Strengthens Hair for less breakage
- Visibly increases hair density & thickness
- Thicker, Stronger, Longer, Hydrated hair
- Promotes Follicle regeneration & Hair Growth
Targeted for hair loss & slowed growth
60 capsules 30-day supply
Target Market(s)
Black/African American Women

```html
<!DOCTYPE html>
<html lang="en">
<head>
<meta charset="utf-8">
<title>Corvane Medical – Root Revival Elevated Label</title>
<link rel="stylesheet" href="https://fonts.googleapis.com/css2?family=Roboto+Condensed:wght@700&family=Montserrat:ital,wght@1,800&family=Open+Sans:wght@400;700&display=swap">
<style>
  :root {
    --page: #ffffff;
    --ink-black: #141414;
    --trapezoid: #1e1e1e;
    --gold-bright: #f6cf1f;
    --gold: #e6ad1e;
    --amber: #b86a22;
    --bronze: #6e3119;
    --bronze-light: #a4602a;
    --band-grey: #3a3d42;
    --orange-top: #eab067;
    --orange-bottom: #c8862c;
    --cream: #fbe8c8;
    --text-brown: #3a1d0c;
    --white: #ffffff;
    --logo-copper: #c8672a;
  }
  * { box-sizing: border-box; margin: 0; padding: 0; }
  html, body {
    width: 1200px; height: 1200px; overflow: hidden;
    background: var(--page);
  }
  .label {
    position: absolute; left: 80px; top: 40px;
    width: 1040px; height: 1120px;
    overflow: hidden;
    background: var(--ink-black);
  }
  .wave-field {
    position: absolute; left: 0; top: 160px; width: 1040px; height: 605px;
    background: linear-gradient(180deg, var(--gold-bright) 0%, var(--gold) 30%, var(--amber) 60%, var(--bronze) 85%, var(--bronze-light) 100%);
  }
  .crest { position: absolute; left: 0; top: 0; }
  .brand {
    position: absolute; left: 0; top: 190px; width: 1040px;
    display: flex; align-items: center; justify-content: center; gap: 16px;
    font-family: "Open Sans", sans-serif; font-weight: 400;
    font-size: 44px; letter-spacing: 2px; color: var(--logo-copper);
  }
  .brand-dot {
    width: 22px; height: 22px; border-radius: 50%;
    background: var(--logo-copper);
  }
  .title {
    position: absolute; left: 0; width: 1040px; text-align: center;
    color: var(--white);
    text-shadow: 0 2px 4px rgba(60, 25, 5, 0.45);
  }
  .title-sub {
    top: 352px;
    font-family: "Roboto Condensed", sans-serif; font-weight: 700; font-size: 72px;
  }
  .title-main {
    top: 420px;
    font-family: "Montserrat", sans-serif; font-style: italic; font-weight: 800;
    font-size: 140px; letter-spacing: -3px; line-height: 1.1;
  }
  .title-formula {
    top: 578px;
    font-family: "Roboto Condensed", sans-serif; font-weight: 700; font-size: 78px;
  }
  .site-band {
    position: absolute; left: 0; top: 765px; width: 1040px; height: 90px;
    background: var(--band-grey);
    display: flex; align-items: center; justify-content: center;
    font-family: "Open Sans", sans-serif; font-weight: 700; font-size: 31px;
    color: var(--white); letter-spacing: 0.5px;
  }
  .benefits-panel {
    position: absolute; left: 0; top: 855px; width: 1040px; height: 265px;
    background: linear-gradient(180deg, var(--orange-top), var(--orange-bottom));
  }
  .benefits {
    position: absolute; left: 140px; top: 22px;
    font-family: "Open Sans", sans-serif;
  }
  .benefits-heading {
    font-weight: 700; font-size: 27px; color: var(--cream); margin-bottom: 12px;
  }
  .benefits-list { list-style: none; }
  .benefits-list li {
    font-size: 23px; line-height: 31px; color: var(--text-brown);
  }
  .benefits-list li::before { content: "- "; }
  .count-badge {
    position: absolute; left: 840px; top: 20px; width: 112px; height: 232px;
    border-radius: 18px; background: var(--band-grey);
    color: var(--white); font-family: "Open Sans", sans-serif;
    display: flex; flex-direction: column; align-items: center;
  }
  .count-number { font-weight: 700; font-size: 72px; line-height: 1; margin-top: 14px; }
  .count-unit { font-size: 24px; margin-top: 2px; }
  .count-rule { width: 90px; height: 2px; background: var(--white); margin: 16px 0 12px; }
  .supply { display: flex; align-items: center; gap: 4px; }
  .supply-days { font-weight: 700; font-size: 44px; line-height: 1; }
  .supply-word { display: flex; flex-direction: column; line-height: 1; }
  .supply-word span:first-child { font-size: 17px; }
  .supply-word span:last-child { font-size: 10px; }
</style>
</head>
<body>
  <main class="label">
    <div class="wave-field" role="img" aria-label="Flowing gold and bronze hair wave lines"></div>

    <svg class="crest" width="1040" height="300" viewBox="0 0 1040 300" aria-hidden="true">
      <polygon points="0,0 1040,0 1040,160 960,160 840,280 200,280 80,160 0,160" fill="var(--trapezoid)"/>
    </svg>

    <div class="brand"><span class="brand-dot"></span>Corvane Medical</div>

    <h1 class="title title-sub">Root Revival</h1>
    <p class="title title-main">ELEVATED</p>
    <p class="title title-formula">Women’s Hair Loss Formula</p>

    <div class="site-band">TARGETED FOR HAIR LOSS &amp; SLOWED GROWTH</div>

    <section class="benefits-panel">
      <div class="benefits">
        <h2 class="benefits-heading">TRACTION ALOPECIA SUPPORT</h2>
        <ul class="benefits-list">
          <li>Prevents hair loss &amp; restores thinning, fragile hair</li>
          <li>Promotes Natural Hair Growth</li>
          <li>Strengthens Hair for less breakage</li>
          <li>Visibly increases hair density &amp; thickness</li>
          <li>Thicker, Stronger, Longer, Hydrated hair</li>
          <li>Promotes Follicle regeneration &amp; Hair Growth</li>
        </ul>
      </div>
      <div class="count-badge">
        <span class="count-number">60</span>
        <span class="count-unit">capsules</span>
        <span class="count-rule"></span>
        <div class="supply">
          <span class="supply-days">30</span>
          <span class="supply-word"><span>DAY</span><span>SUPPLY</span></span>
        </div>
      </div>
    </section>
  </main>
</body>
</html>
```